Business Card Design for company

We want new business cards. We'd like something different-- yet still highly professional. Our tagline is Building strategy, advancing results. Stock photos are ok, as long as they are relevant and look upscale.

Target Market(s)

Architecture/Business Management Consulting/Engineering Consulting

Contact Information for Business Card

dark gray background with pops of blue might be good, but you tell me. You're the designers. Rounded corners might be nice, but again, you tell me.

Font styles to use
Serif
Sans Serif

Colors
3276b5
5c5c5c
9d9d9d
fbfbfb

Requirements
Nice to have
• Something different, but still very professional.

```html
<!DOCTYPE html>
<html lang="en">
<head>
<meta charset="utf-8">
<title>Velorin Group – Business Card</title>
<link rel="stylesheet" href="https://fonts.googleapis.com/css2?family=Lato:ital,wght@0,400;0,700;1,400&display=swap">
<style>
  :root {
    --stage: #3b3b3b;
    --card: #1f1f20;
    --blue: #3276b5;
    --mid-gray: #5c5c5c;
    --light-gray: #9d9d9d;
    --white: #fbfbfb;
  }
  * { box-sizing: border-box; margin: 0; padding: 0; }
  html, body {
    width: 1200px; height: 755px; overflow: hidden;
    background: var(--stage);
    font-family: "Lato", Arial, sans-serif;
  }
  .canvas { position: relative; width: 1200px; height: 755px; }
  .card {
    position: absolute; top: 212px; height: 304px;
    background: var(--card); border-radius: 12px; overflow: hidden;
  }
  .card--front { left: 73px; width: 525px; border-top: 8px solid var(--blue); }
  .card--back { left: 622px; width: 502px; }

  .holder { position: absolute; left: 22px; top: 42px; color: var(--white); }
  .holder__name { font-size: 23px; font-weight: 400; letter-spacing: 0.2px; line-height: 28px; }
  .holder__name strong { font-weight: 700; }
  .holder__title { font-size: 13px; font-style: italic; color: var(--light-gray); margin-top: 0; line-height: 16px; }

  .contact { position: absolute; left: 22px; list-style: none; color: var(--light-gray); font-size: 14px; letter-spacing: 0.4px; }
  .contact li { display: flex; line-height: 19px; }
  .contact svg { flex: none; width: 11px; height: 11px; margin: 4px 8px 0 0; fill: var(--blue); }
  .contact--main { top: 114px; }
  .contact--web { top: 235px; font-size: 13px; }
  .contact--web li { line-height: 17px; }

  .brand-mark {
    position: absolute; right: 30px; bottom: 28px;
    font-size: 26px; font-weight: 700; color: var(--blue); letter-spacing: 1px; line-height: 1;
  }

  .brand-large {
    position: absolute; left: 0; right: 0; top: 98px; text-align: center;
    font-size: 78px; font-weight: 700; color: var(--blue); letter-spacing: 2px; line-height: 1;
  }
  .brand-large__sub {
    position: absolute; left: 0; right: 0; top: 188px; text-align: center;
    font-size: 22px; font-weight: 700; color: var(--blue); letter-spacing: 3px; line-height: 1;
  }
  .tagline {
    position: absolute; left: 0; right: 0; top: 258px; text-align: center;
    font-size: 16px; font-weight: 700; color: var(--white); letter-spacing: 2.6px; line-height: 20px;
  }
</style>
</head>
<body>
<main class="canvas">
  <section class="card card--front" aria-label="Card front">
    <div class="holder">
      <h1 class="holder__name">John <strong>Smith</strong></h1>
      <p class="holder__title">Tile ges here</p>
    </div>
    <ul class="contact contact--main">
      <li><svg viewBox="0 0 12 12"><path d="M1 4c0-2 2-3 5-3s5 1 5 3l-2 1-1-2H4L3 5z M2 6h8l1 5H1z"/></svg>123-456-7890</li>
      <li><svg viewBox="0 0 12 12"><path d="M6 1l6 5h-2v5H7V8H5v3H2V6H0z"/></svg><span>Street address goes here,<br>Suite #303, Alt Bldg,<br>NY 82365</span></li>
    </ul>
    <ul class="contact contact--web">
      <li><svg viewBox="0 0 12 12"><path d="M0 2h12v1L6 7 0 3z M0 4l6 4 6-4v6H0z"/></svg>yourdomain.com</li>
      <li><svg viewBox="0 0 12 12"><path d="M5 7l2-2M4 5L2 7a1.8 1.8 0 0 0 3 3l2-2M8 7l2-2a1.8 1.8 0 0 0-3-3L5 4" fill="none" stroke="#3276b5" stroke-width="1.5"/></svg>yourname@yourdomain.com</li>
    </ul>
    <p class="brand-mark">VELORIN</p>
  </section>

  <section class="card card--back" aria-label="Card back">
    <p class="brand-large">VELORIN</p>
    <p class="brand-large__sub">GROUP</p>
    <p class="tagline">BUILDING STRATEGY, ADVANCING RESULTS.</p>
  </section>
</main>
</body>
</html>
```